Oven Cleaning Business owner needs business card design

Hi there,
Would like for a business card to be designed for myself, the owner of a professional oven cleaning business on the Sunshine Coast.
Would like it to look sleek, and modern-ish. Bit creative is encouraged too.
Include following:
Name/title: Corin ter Haghe, Owner
Phone number: 1300 482 916
Email: info@hearthshinecrew.com.au
Website: www.hearthshinecrew.com.au

```html
<!DOCTYPE html>
<html lang="en">
<head>
<meta charset="utf-8">
<title>Hearthshine Crew – Business Card</title>
<link rel="stylesheet" href="https://fonts.googleapis.com/css2?family=Krona+One&family=Raleway:wght@300;400&display=swap">
<style>
  :root {
    --stage: #4a6cff;
    --paper: #ffffff;
    --ink: #0a0c10;
    --navy-deep: #0b2a62;
    --navy-light: #4a6490;
    --teal: #5ef5c4;
    --back-blue: #0a56c8;
  }
  * { box-sizing: border-box; margin: 0; padding: 0; }
  html, body {
    width: 1200px; height: 1200px; overflow: hidden;
    background: var(--stage);
  }
  .stage { position: relative; width: 1200px; height: 1200px; }

  .card { position: absolute; overflow: hidden; }

  .card-front { left: 227px; top: 87px; width: 718px; height: 471px; background: var(--paper); }
  .front-bg { position: absolute; inset: 0; width: 100%; height: 100%; }

  .front-title {
    position: absolute; left: 29px; top: 60px;
    font-family: "Krona One", sans-serif;
    font-size: 23px; line-height: 37px; letter-spacing: 1px;
    color: var(--ink); text-transform: uppercase;
  }

  .contact-list { position: absolute; left: 28px; top: 0; list-style: none; }
  .contact-item {
    position: absolute; left: 0; display: flex; align-items: center;
    white-space: nowrap;
    font-family: "Raleway", sans-serif; font-weight: 300;
    font-size: 24px; color: var(--ink);
  }
  .contact-item.name { top: 220px; font-weight: 400; }
  .contact-item.phone { top: 269px; }
  .contact-item.email { top: 317px; }
  .contact-item.web { top: 365px; }
  .contact-icon { width: 25px; height: 25px; margin-right: 17px; flex: none; }

  .illustration-slot {
    position: absolute; left: 453px; top: 118px; width: 236px; height: 311px;
    border-radius: 6px;
    background: linear-gradient(160deg, rgba(255,255,255,0.10), rgba(255,255,255,0.04));
  }

  .brand-front {
    position: absolute; left: 486px; top: 26px;
    display: flex; align-items: center; gap: 10px;
  }
  .brand-dot { border-radius: 50%; background: var(--teal); flex: none; }
  .brand-front .brand-dot { width: 40px; height: 40px; }
  .brand-name {
    font-family: "Krona One", sans-serif; text-transform: uppercase;
    line-height: 1.25;
  }
  .brand-front .brand-name { font-size: 14px; color: var(--teal); }

  .card-back { left: 225px; top: 622px; width: 719px; height: 471px; background: var(--back-blue); }
  .brand-back {
    position: absolute; left: 0; right: 0; top: 123px;
    display: flex; flex-direction: column; align-items: center; gap: 48px;
  }
  .brand-back .brand-dot { width: 110px; height: 110px; }
  .brand-back .brand-name { font-size: 20px; color: var(--ink); letter-spacing: 1px; }
</style>
</head>
<body>
<main class="stage">

  <section class="card card-front">
    <svg class="front-bg" viewBox="0 0 1157 758" preserveAspectRatio="none" aria-hidden="true">
      <defs>
        <linearGradient id="navyFade" x1="0" y1="1" x2="1" y2="0">
          <stop offset="0.3" stop-color="var(--navy-deep)"/>
          <stop offset="1" stop-color="var(--navy-light)"/>
        </linearGradient>
      </defs>
      <polygon points="547,0 1157,0 1157,758 713,758" fill="var(--ink)"/>
      <polygon points="578,0 1157,0 1157,758 743,758" fill="url(#navyFade)"/>
    </svg>

    <h1 class="front-title">Oven Cleaner<br>Sunshine Coast</h1>

    <ul class="contact-list">
      <li class="contact-item name">
        <svg class="contact-icon" viewBox="0 0 24 24" aria-hidden="true"><circle cx="12" cy="12" r="12" fill="var(--ink)"/><circle cx="12" cy="9" r="3.6" fill="#fff"/><path d="M5.8 18.2c.6-3.3 3.2-4.8 6.2-4.8s5.6 1.5 6.2 4.8z" fill="#fff"/></svg>
        Corin ter Haghe
      </li>
      <li class="contact-item phone">
        <svg class="contact-icon" viewBox="0 0 24 24" aria-hidden="true"><circle cx="12" cy="12" r="12" fill="var(--ink)"/><path d="M8.2 6.5l2 2.4-1.2 1.3c.8 1.7 2 2.9 3.6 3.7l1.3-1.2 2.4 2-1.4 2c-4.1-.4-7.8-4.1-8.3-8.3z" fill="#fff"/></svg>
        1300 482 916
      </li>
      <li class="contact-item email">
        <svg class="contact-icon" viewBox="0 0 24 24" aria-hidden="true"><circle cx="12" cy="12" r="12" fill="var(--ink)"/><rect x="6" y="8" width="12" height="8.5" fill="#fff"/><path d="M6 8l6 5 6-5M6 16.5l4.3-4.3M18 16.5l-4.3-4.3" stroke="var(--ink)" stroke-width="0.9" fill="none"/></svg>
        info@hearthshinecrew.com.au
      </li>
      <li class="contact-item web">
        <svg class="contact-icon" viewBox="0 0 24 24" aria-hidden="true"><circle cx="12" cy="12" r="12" fill="var(--ink)"/><g stroke="#fff" stroke-width="1" fill="none"><circle cx="12" cy="12" r="6"/><ellipse cx="12" cy="12" rx="2.6" ry="6"/><path d="M6 12h12M7 9h10M7 15h10"/></g></svg>
        www.hearthshinecrew.com.au
      </li>
    </ul>

    <div class="illustration-slot" role="img" aria-label="Line drawing of a smiling oven cleaner giving a thumbs up beside a wall oven"></div>

    <div class="brand-front">
      <span class="brand-dot" aria-hidden="true"></span>
      <span class="brand-name">Hearthshine<br>Crew</span>
    </div>
  </section>

  <section class="card card-back">
    <div class="brand-back">
      <span class="brand-dot" aria-hidden="true"></span>
      <span class="brand-name">Hearthshine Crew</span>
    </div>
  </section>

</main>
</body>
</html>
```